Mental Health Services for Employees - we need a website for our new business

We need a simple web design to showcase our various services. Our programs help organizations to ensure the heath and wellness of their workers. Our company is called "Harborline Workforce Solutions Inc." or "Harborline" We'd like to see designs that use the colour palette from our logo. Our customers our fairly conservative, and our design should communicate due diligence around providing a safe and healthy environment for workers. Attached our the logo files. Also sample photographs from our purchased images - others available. Original design for website is found here: https://pondlark7.sitebrook.example/page-1 A key page not listed in our original design is a section that lists "Five Reasons to Work With Us". We will need to be able to modify and change the copy/menu options as the business grows.

Target Market(s)

businesses who want to provide health and wellness services for their employees

Coding

Coded - Design and coding required

Number of Pages Required

2 page

Font styles to use
Sans Serif

Requirements
Must have
• colours that work with our attached logo

```html
<!DOCTYPE html>
<html lang="en">
<head>
<meta charset="utf-8">
<title>Harborline Workforce Solutions</title>
<link rel="stylesheet" href="https://fonts.googleapis.com/css2?family=Barlow:ital,wght@0,400;0,500;0,600;0,700;1,400&display=swap">
<style>
:root{
  --orange:#f2a227;
  --teal:#1b9e8a;
  --green:#1f7e5a;
  --ink:#2b2b2b;
  --body:#4a4a4a;
  --muted:#6d6d6d;
  --grey:#f3f3f3;
  --line:#dcdcdc;
  --white:#fff;
}
*{box-sizing:border-box;margin:0;padding:0}
html,body{width:1200px;height:4304px;overflow:hidden}
body{position:relative;font-family:'Barlow',sans-serif;color:var(--body);background:var(--white)}
.abs{position:absolute}
.brand{display:flex;align-items:center;gap:10px;font-weight:700;color:var(--ink);font-size:30px;letter-spacing:.2px}
.brand-square{width:22px;height:22px;background:var(--teal)}
/* header */
.site-header{left:0;top:0;width:1200px;height:95px;background:var(--white)}
.site-header .brand{position:absolute;left:172px;top:28px}
.main-nav{position:absolute;left:418px;top:0;display:flex;height:95px;align-items:center;font-size:15px;font-weight:500;color:var(--ink)}
.main-nav a{text-decoration:none;color:inherit;padding:0 17px;height:95px;display:flex;align-items:center}
.main-nav a.active{background:var(--orange);color:var(--white);padding:0 22px}
/* hero */
.hero{left:0;top:95px;width:1200px;height:607px;background:linear-gradient(120deg,#c9cdd6 0%,#8d93a3 40%,#c3b9ae 70%,#d9dde6 100%)}
.hero-accent{position:absolute;right:0;top:250px;width:90px;height:90px;background:var(--teal)}
.slider-dots{position:absolute;display:flex;gap:5px}
.slider-dots span{width:12px;height:6px;background:var(--white);opacity:.9}
.slider-dots span.on{background:var(--teal)}
/* about */
.about-photo{left:127px;top:827px;width:413px;height:363px}
.about-photo .frame-teal{position:absolute;left:0;top:150px;width:40px;height:213px;background:var(--teal)}
.about-photo .frame-orange{position:absolute;right:0;top:0;width:10px;height:210px;background:var(--orange);transform:skewX(-3deg)}
.about-photo .photo{position:absolute;left:30px;top:0;width:368px;height:363px;background:linear-gradient(160deg,#b9c6cf 0%,#e3b63a 35%,#8a6b52 60%,#dfe23a 100%);clip-path:polygon(5% 0,100% 0,100% 100%,0 100%,0 25%)}
.section-title{display:flex;align-items:center;gap:10px;font-weight:700;color:var(--ink);text-transform:uppercase}
.mark{display:inline-block;width:14px;height:14px;background:var(--orange)}
.about-text{left:588px;top:848px;width:440px}
.about-text h2{font-size:30px;margin-bottom:20px}
.about-text p{font-size:11.5px;line-height:20px;color:var(--body);margin-bottom:19px}
/* reasons */
.reasons{left:0;top:1257px;width:1200px;height:643px}
.reasons svg{position:absolute;left:0;top:0}
.reasons h2{position:absolute;left:0;top:145px;width:1200px;justify-content:center;font-size:30px;color:var(--white)}
.reasons .mark{background:var(--orange)}
.reason{position:absolute;top:255px;width:170px;color:var(--white)}
.reason svg{position:static;display:block;height:68px;width:68px;margin-bottom:20px}
.reason h3{font-size:16px;font-weight:600;margin-bottom:12px}
.reason p{font-size:11px;line-height:19.5px;opacity:.92}
/* services */
.services-bg{left:0;top:1838px;width:1200px;height:740px}
.services h2,.gallery h2{position:absolute;left:0;width:1200px;justify-content:center;font-size:30px}
.card{position:absolute;top:2030px;width:273px;height:391px;background:var(--white);border:1px solid #e4e4e4}
.card .photo{height:204px}
.card h3{font-size:16.5px;font-weight:700;color:var(--ink);margin:26px 26px 12px;line-height:21px}
.card p{font-size:11px;line-height:19.5px;margin:0 26px;color:var(--body)}
.btn{position:absolute;left:26px;top:328px;width:108px;height:30px;color:var(--white);font-size:10.5px;font-weight:700;display:flex;align-items:center;justify-content:center;clip-path:polygon(10% 0,100% 0,90% 100%,0 100%);text-decoration:none}
.btn.orange{background:var(--orange)}
.btn.teal{background:var(--teal)}
/* gallery */
.gallery-intro{left:300px;top:2683px;width:600px;text-align:center;font-size:11.5px;line-height:20px}
.tile{position:absolute}
/* testimonial */
.testimonial{left:0;top:3360px;width:1200px;height:560px}
.quote-mark{left:278px;top:3520px;font-size:150px;line-height:1;font-weight:700;color:var(--orange);font-family:'Barlow',sans-serif}
.quote-text{left:391px;top:3560px;width:540px;color:#e6e6e6;font-style:italic;font-size:19px;line-height:28px}
.quote-author{left:391px;top:3727px;color:var(--orange);font-weight:600;font-size:18px}
.arrows{left:988px;top:3782px}
/* footer */
.site-footer .brand{position:absolute;left:172px;top:3937px;font-size:26px}
.partner{position:absolute;top:3920px;height:56px}
.footer-rule{left:172px;top:4010px;width:856px;height:1px;background:var(--line)}
.footer-col{position:absolute;top:4036px;font-size:11.5px;color:var(--body)}
.footer-col h4{font-size:14px;font-weight:500;color:var(--ink);margin-bottom:20px}
.footer-col li{list-style:none;line-height:20px}
.contact-row{display:flex;gap:14px;margin-bottom:14px;line-height:18px}
.contact-row svg{flex:0 0 22px}
.copyright{left:172px;top:4263px;font-size:11.5px;color:var(--ink)}
.social{left:913px;top:4252px;display:flex;gap:7px}
.social span{width:23px;height:23px;border-radius:50%;background:var(--teal)}
.social span.alt{background:var(--orange)}
</style>
</head>
<body>

<header class="abs site-header">
  <div class="brand"><span class="brand-square"></span>Harborline</div>
  <nav class="main-nav">
    <a class="active" href="#">HOME</a>
    <a href="#">SERVICES</a>
    <a href="#">ABOUT</a>
    <a href="#">SAP</a>
    <a href="#">REFERRALS</a>
    <a href="#">CONTACT</a>
    <a href="#">PORTAL</a>
  </nav>
</header>

<section class="abs hero" role="img" aria-label="Photo of two women in conversation during a counselling session">
  <div class="hero-accent"></div>
  <div class="slider-dots" style="left:563px;top:570px"><span></span><span></span><span class="on"></span><span></span><span></span></div>
</section>

<div class="abs about-photo">
  <div class="frame-teal"></div>
  <div class="frame-orange"></div>
  <div class="photo" role="img" aria-label="Photo of construction workers in hard hats and safety vests"></div>
</div>
<section class="abs about-text">
  <h2 class="section-title"><span class="mark"></span>About</h2>
  <p>Harborline Workforce Solutions Inc. (“Harborline”) provides outstanding business-to-business services that support and promote health, wellness, and safety in the workplace. Harborline’s flagship programs are the Substance Abuse Professional (SAP) and Specialized Addiction Case Management services.</p>
  <p>Harborline is ready to provide organizations with access to a suite of best-practice solutions and options for your employees. These services empower organizations to effectively deal with substance use, to understand and fulfill various legislative and/or policy requirements, and to help keep their workers safe and healthy.</p>
  <p>Whenever organizations have a need to address substance use in the workplace please consider us a resource to help with program development based on the locations and specific needs of your employees.</p>
</section>

<section class="abs reasons">
  <svg width="1200" height="643" viewBox="0 0 1200 643" aria-hidden="true">
    <polygon points="0,43 1200,0 1200,589 0,643" fill="#1b9e8a"/>
    <polygon points="0,43 440,28 0,80" fill="#1f7e5a"/>
    <polygon points="0,58 440,44 0,360" fill="#f2a227"/>
    <polygon points="520,643 1200,589 1200,622" fill="#f2a227"/>
  </svg>
  <h2 class="section-title">Five Reasons <span class="mark"></span> To Work With Us</h2>

  <div class="reason" style="left:172px">
    <svg viewBox="0 0 68 68" fill="none" stroke="#fff" stroke-width="2.2"><path d="M6 62 L26 30 L34 42 L40 34 L62 62 Z"/><path d="M26 30 V6 L42 11 L26 16"/></svg>
    <h3>1.Suptacuntium</h3>
    <p>Sed ut perspiciatis unde os iste natuserror sit voluptiom accusantium dolorlaloru dlu mtotam rem aperiamcusntm dolorlaloru daliu mtlootamig aperi, eaquea uaevtor.</p>
  </div>
  <div class="reason" style="left:351px">
    <svg viewBox="0 0 68 68" fill="none" stroke="#fff" stroke-width="2.2"><circle cx="34" cy="34" r="30"/><path d="M34 12 V34 L48 46"/></svg>
    <h3>2.Louptuntium</h3>
    <p>Sed ut perspiciatis unde os iste natuserror sit voluptiom accusantium dolorlaloru dlu mtotam rem aperiamcusntm dolorlaloru daliu mtlootamig aperi, eaquea uaevtor.</p>
  </div>
  <div class="reason" style="left:530px">
    <svg viewBox="0 0 68 68" fill="none" stroke="#fff" stroke-width="2.2"><path d="M20 62 V50 C10 44 8 32 12 22 C18 8 40 4 50 16 C56 24 54 30 56 36 L60 42 L54 44 V52 L44 52 V62"/><circle cx="34" cy="24" r="10"/></svg>
    <h3>3.Guptasantiu</h3>
    <p>Sed ut perspiciatis unde os iste natuserror sit voluptiom accusantium dolorlaloru dlu mtotam rem aperiamcusntm dolorlaloru daliu mtlootamig aperi, eaquea uaevtor.</p>
  </div>
  <div class="reason" style="left:709px">
    <svg viewBox="0 0 68 68" fill="none" stroke="#fff" stroke-width="2.2"><ellipse cx="34" cy="38" rx="24" ry="18"/><path d="M20 54 V62 M46 54 V62"/><circle cx="36" cy="12" r="7"/></svg>
    <h3>4.Suptacutium</h3>
    <p>Sed ut perspiciatis unde os iste natuserror sit voluptiom accusantium dolorlaloru dlu mtotam rem aperiamcusntm dolorlaloru daliu mtlootamig aperi, eaquea uaevtor.</p>
  </div>
  <div class="reason" style="left:887px">
    <svg viewBox="0 0 68 68" fill="none" stroke="#fff" stroke-width="2.2"><circle cx="30" cy="38" r="26"/><circle cx="30" cy="38" r="16"/><circle cx="30" cy="38" r="6"/><path d="M30 38 L58 10 M50 10 H58 V18"/></svg>
    <h3>5.Suptacusantiu</h3>
    <p>Sed ut perspiciatis unde os iste natuserror sit voluptiom accusantium dolorlaloru dlu mtotam rem aperiamcusntm dolorlaloru daliu mtlootamig aperi, eaquea uaevtor.</p>
  </div>
</section>

<div class="abs services-bg" aria-hidden="true">
  <svg width="1200" height="740" viewBox="0 0 1200 740"><polygon points="0,62 1200,62 1200,668 0,735" fill="#f3f3f3"/></svg>
</div>
<section class="services">
  <h2 class="section-title abs" style="top:1948px">Our <span class="mark"></span> Services</h2>
  <article class="card" style="left:172px">
    <div class="photo" role="img" aria-label="Photo of pilots at the controls in an aircraft cockpit" style="background:linear-gradient(160deg,#3c5672,#2a3440 60%,#7b8a96)"></div>
    <h3>Accomodation Screening</h3>
    <p>Sed ut perspiciatis unde os iste natuserror sit voluptiom accusantium dolorlaloru dlu mtotam rem aperiamcusntm.</p>
    <a class="btn orange" href="#">READ MORE</a>
  </article>
  <article class="card" style="left:463px">
    <div class="photo" role="img" aria-label="Photo of a smiling support agent wearing a headset" style="background:linear-gradient(160deg,#b9b1a8,#7a6c62 55%,#dcd6cf)"></div>
    <h3>SAP Assessments</h3>
    <p>Sed ut perspiciatis unde os iste natuserror sit voluptiom accusantium dolorlaloru dlu mtotam rem aperiamcusntm.</p>
    <a class="btn teal" href="#">READ MORE</a>
  </article>
  <article class="card" style="left:752px">
    <div class="photo" role="img" aria-label="Photo of site workers in safety vests reviewing plans near an excavator" style="background:linear-gradient(160deg,#9cc3e0,#c8d24a 50%,#a89070)"></div>
    <h3>Specialized Addiction<br>Case Management</h3>
    <p>Sed ut perspiciatis unde os iste natuserror sit voluptiom accusantium dolorlaloru.</p>
    <a class="btn teal" href="#">READ MORE</a>
  </article>
</section>

<section class="gallery">
  <h2 class="section-title abs" style="top:2617px">Our <span class="mark"></span> Gallery</h2>
  <p class="abs gallery-intro">Sed ut perspiciatis unde os iste natuserror sit voluptiom accusantium dolorlaloru dlu mtotam rem aperiamcu sntm. Sed ut perspiciatis unde os iste natuserror sit voluptiom accusantium dolorlaloru dlu.</p>
  <div class="tile" role="img" aria-label="Photo of a forestry worker cutting a log with a chainsaw" style="left:172px;top:2745px;width:543px;height:251px;background:linear-gradient(135deg,#5a6650,#8a8c7c 45%,#b44a2a 70%,#4c5442)"></div>
  <div class="tile" role="img" aria-label="Photo of a worker in an orange jacket and hard hat" style="left:729px;top:2745px;width:297px;height:251px;background:linear-gradient(135deg,#8d9499,#d9772c 55%,#6e6a5e)"></div>
  <div class="tile" role="img" aria-label="Photo of two workers silhouetted beside an oil pump jack at dusk" style="left:172px;top:3009px;width:266px;height:251px;background:linear-gradient(180deg,#2c4f8f,#5d86c0 55%,#13213a)"></div>
  <div class="tile" role="img" aria-label="Photo of a large mining haul truck" style="left:449px;top:3009px;width:266px;height:251px;background:linear-gradient(180deg,#a9acb2,#c99a6e 55%,#5b4a3a)"></div>
  <div class="tile" role="img" aria-label="Photo of a red freight locomotive under a sunset sky" style="left:729px;top:3009px;width:297px;height:251px;background:linear-gradient(180deg,#e08a5a,#b4513a 55%,#3a2a24)"></div>
  <div class="slider-dots" style="left:563px;top:3294px"><span style="background:#555"></span><span style="background:#555"></span><span class="on"></span><span style="background:#555"></span><span style="background:#555"></span></div>
</section>

<section class="abs testimonial">
  <svg width="1200" height="560" viewBox="0 0 1200 560" role="img" aria-label="Dark background photo of an open road stretching to the horizon">
    <defs><linearGradient id="road" x1="0" y1="0" x2="0" y2="1"><stop offset="0" stop-color="#6b6e70"/><stop offset=".5" stop-color="#3e4143"/><stop offset="1" stop-color="#2a2c2d"/></linearGradient></defs>
    <polygon points="0,132 1200,10 1200,483 0,550" fill="url(#road)"/>
    <polygon points="640,515 1200,478 1200,496 700,520" fill="#1b9e8a"/>
  </svg>
</section>
<div class="abs quote-mark" aria-hidden="true">“</div>
<blockquote class="abs quote-text">Sed ut perspiciatis unde omnis iste natus error sit voluptatem accusantium doloremque laudantium, totam rem aperiam, eaque ipsa quae ab illo inventore veritatis et quasi architecto beatae vit ae dicta sunt explicabo. Nemo enim ipsam voluptatem quia volupt as sit aspernatur aut odit aut fugit, sed quia consequuntur eos ratione voluptatem sequi nesciunt.</blockquote>
<div class="abs quote-author">- Alex Morgan City Name</div>
<svg class="abs arrows" width="44" height="30" viewBox="0 0 44 30" fill="none" stroke="#bbb" stroke-width="1.5" aria-hidden="true"><path d="M14 2 L2 15 L14 28 M30 2 L42 15 L30 28"/></svg>

<footer class="site-footer">
  <div class="brand"><span class="brand-square"></span>Harborline</div>
  <div class="partner" style="left:745px;width:140px;border:2px solid #999;background:#fff"></div>
  <div class="partner" style="left:888px;width:139px;background:#111"></div>
  <div class="abs footer-rule"></div>

  <div class="footer-col" style="left:172px;width:230px">
    <h4>Contact</h4>
    <div class="contact-row">
      <svg viewBox="0 0 22 22" width="22" height="22" fill="none" stroke="#1b9e8a" stroke-width="1.5"><path d="M11 20 C5 13 4 10 4 8 A7 7 0 0 1 18 8 C18 10 17 13 11 20 Z"/><circle cx="11" cy="8" r="2.5"/></svg>
      <div>418 Marlow Avenue, Suite 210,<br>Kingsport Ontario, K2P 4R8</div>
    </div>
    <div class="contact-row">
      <svg viewBox="0 0 22 22" width="22" height="22" fill="none" stroke="#1b9e8a" stroke-width="1.5"><path d="M5 3 L9 3 L10 8 L7.5 9.5 A12 12 0 0 0 12.5 14.5 L14 12 L19 13 L19 17 C19 18 18 19 17 19 C9 19 3 13 3 5 C3 4 4 3 5 3 Z"/></svg>
      <div>555-013-4471<br>555-014-8820</div>
    </div>
    <div class="contact-row">
      <svg viewBox="0 0 22 22" width="22" height="22" fill="none" stroke="#1b9e8a" stroke-width="1.5"><rect x="2" y="5" width="18" height="12"/><path d="M2 5 L11 12 L20 5"/></svg>
      <div>Email:<br>coordinators@harborline-ws.example</div>
    </div>
  </div>
  <div class="footer-col" style="left:439px">
    <h4>Projects</h4>
    <ul><li>Lorem ipsum dolo</li><li>Consectetur adipiscing elit,</li><li>Fusce eget leo tincid</li><li>Donec consequat</li><li>Praesent elementum</li><li>Jmauris posueret</li><li>Aenean a ex eu lectu</li></ul>
  </div>
  <div class="footer-col" style="left:657px">
    <h4>Company</h4>
    <ul><li>Lorem ipsum dolo</li><li>Consectetur adipiscing elit,</li><li>Fusce eget leo tincid</li><li>Donec consequat</li><li>Praesent elementum</li><li>Jmauris posueret</li><li>Aenean a ex eu lectu</li></ul>
  </div>
  <div class="footer-col" style="left:886px">
    <h4>Other Links</h4>
    <ul><li>Lorem ipsum dolo</li><li>Consectetur adipiscing elit,</li><li>Fusce eget leo tincid</li><li>Donec consequat</li><li>Praesent elementum</li><li>Jmauris posueret</li><li>Aenean a ex eu lectu</li></ul>
  </div>
  <div class="abs copyright">Copyright 2019 All Rights Reserved</div>
  <div class="abs social" aria-label="Social links"><span></span><span></span><span></span><span class="alt"></span></div>
</footer>

</body>
</html>
```